Commercial / Truck Battery Label

We need a high definition label design to send to a commercial printer for a Commercial/Truck Battery Label
I will upload our current truck battery label for you to get an idea of what we are looking for. Along with some competitor images and other logos for the label that we have on file. If we need to purchase a few images to make the label we can do that but need to see the design first.
The Labels need to have a plain white area which is 60mm Long x 40mm High along the bottom left corner. We will use this area for the battery specifications.
The Top Six Warning Icons downloaded also need to be on the label, perhaps along the bottom to the right of the white area in pairs. The icons size can be between 10mm x 10mm and 20mm x 20mm
The dimensions of the label need to be 390mm Long and the height needs to be both 140mm and 180mm. Same label 2 different sizes.
I would like to keep the terms : "SUPER HEAVY DUTY" and "THE STEADY CHARGE THAT HOLDS" on the label somewhere. Maybe replacing the word batteries or commercial with SUPER HEAVY DUTY under the right side of the VOLTMASTRO Logo.
The labels will be used predominantly on Black batteries, so a colour scheme or design to suit that.
I don't mind a completely fresh design or a reworking of the old design.
Look and feel
Each slider illustrates characteristics of the customer's brand and the style your logo design should communicate.

```html
<!DOCTYPE html>
<html lang="en">
<head>
<meta charset="utf-8">
<title>VOLTMASTRO Super Heavy Duty Battery Labels</title>
<link href="https://fonts.googleapis.com/css2?family=Anton&family=Roboto:wght@400;700&display=swap" rel="stylesheet">
<style>
  :root {
    --stage: #efefef;
    --label-black: #111214;
    --label-red: #e0001b;
    --label-blue: #0d3a8c;
    --label-white: #ffffff;
    --spec-grey: #e4e4e4;
    --ink: #1a1a1a;
  }
  html, body {
    margin: 0;
    width: 1200px;
    height: 1158px;
    overflow: hidden;
    background: var(--stage);
  }
  .label {
    position: absolute;
    left: 0; top: 0;
    width: 902px;
    box-shadow: 0 3px 8px rgba(0,0,0,0.35);
  }
  .label--tall { left: 152px; top: 150px; height: 420px; }
  .label--short { left: 148px; top: 682px; height: 324px; }
  .label svg { display: block; width: 100%; height: 100%; }
  .headline { font-family: "Anton", sans-serif; }
  .headline--slanted { font-style: italic; }
  .icon-caption { font-family: "Roboto", sans-serif; font-weight: 700; fill: var(--label-white); }
  .spec {
    position: absolute;
    left: 22px;
    font-family: "Roboto", sans-serif;
    color: var(--ink);
  }
  .spec__title { font-weight: 700; margin: 0; }
  .spec__body { margin: 0; }
  .label--tall .spec { top: 359px; width: 490px; }
  .label--tall .spec__title { font-size: 11px; line-height: 14px; }
  .label--tall .spec__body { font-size: 9px; line-height: 12px; }
  .label--short .spec { top: 283px; width: 560px; }
  .label--short .spec__title { font-size: 9px; line-height: 11px; }
  .label--short .spec__body { font-size: 7.6px; line-height: 10px; }
</style>
</head>
<body>

<svg width="0" height="0" style="position:absolute" aria-hidden="true">
  <defs>
    <symbol id="icon-manual" viewBox="0 0 40 40">
      <circle cx="20" cy="20" r="18" fill="#111214" stroke="#fff" stroke-width="2"/>
      <rect x="13" y="10" width="14" height="19" fill="none" stroke="#fff" stroke-width="2"/>
      <path d="M16 15h8M16 19h8M16 23h6" stroke="#fff" stroke-width="1.6"/>
    </symbol>
    <symbol id="icon-goggles" viewBox="0 0 40 40">
      <circle cx="20" cy="20" r="18" fill="#111214" stroke="#fff" stroke-width="2"/>
      <rect x="10" y="16" width="9" height="7" rx="3" fill="none" stroke="#fff" stroke-width="2"/>
      <rect x="21" y="16" width="9" height="7" rx="3" fill="none" stroke="#fff" stroke-width="2"/>
      <path d="M19 19h2M8 18h2M30 18h2" stroke="#fff" stroke-width="2"/>
    </symbol>
    <symbol id="icon-children" viewBox="0 0 40 40">
      <circle cx="20" cy="20" r="18" fill="#fff" stroke="#111214" stroke-width="2"/>
      <circle cx="20" cy="12" r="3" fill="#111214"/>
      <path d="M20 16v9M15 19h10M20 25l-4 6M20 25l4 6" stroke="#111214" stroke-width="2.4"/>
      <circle cx="20" cy="20" r="14" fill="none" stroke="#e0001b" stroke-width="3"/>
      <path d="M10 10l20 20" stroke="#e0001b" stroke-width="3"/>
    </symbol>
    <symbol id="icon-acid" viewBox="0 0 40 40">
      <circle cx="20" cy="20" r="18" fill="#111214" stroke="#fff" stroke-width="2"/>
      <path d="M10 26h14l6-4v6H10z" fill="#fff"/>
      <path d="M18 9c2 3 3 5 3 7a3 3 0 0 1-6 0c0-2 1-4 3-7z" fill="#fff"/>
    </symbol>
    <symbol id="icon-explosive" viewBox="0 0 40 40">
      <circle cx="20" cy="20" r="18" fill="#fff" stroke="#111214" stroke-width="2"/>
      <path d="M12 29l9-9" stroke="#111214" stroke-width="3"/>
      <path d="M21 20l2-9 2 6 4-4-2 7 5-1-6 4" fill="none" stroke="#111214" stroke-width="1.8"/>
    </symbol>
    <symbol id="icon-noflame" viewBox="0 0 40 40">
      <circle cx="20" cy="20" r="18" fill="#fff" stroke="#111214" stroke-width="2"/>
      <path d="M20 10c4 5 6 8 6 12a6 6 0 0 1-12 0c0-3 2-5 3-7 1 2 2 3 3 3 0-3-1-5 0-8z" fill="#111214"/>
      <circle cx="20" cy="20" r="14" fill="none" stroke="#e0001b" stroke-width="3"/>
      <path d="M10 10l20 20" stroke="#e0001b" stroke-width="3"/>
    </symbol>
    <linearGradient id="tractor-tones" x1="0" y1="0" x2="0" y2="1">
      <stop offset="0" stop-color="#a9cbe9"/>
      <stop offset="0.5" stop-color="#8fae6a"/>
      <stop offset="1" stop-color="#4d7a2e"/>
    </linearGradient>
    <linearGradient id="truck-tones" x1="0" y1="0" x2="1" y2="1">
      <stop offset="0" stop-color="#7c8c99"/>
      <stop offset="0.45" stop-color="#e88a1c"/>
      <stop offset="1" stop-color="#555b62"/>
    </linearGradient>
  </defs>
</svg>

<!-- 180 mm label -->
<section class="label label--tall">
  <svg viewBox="0 0 902 420" xmlns="http://www.w3.org/2000/svg">
    <rect class="label__base" width="902" height="420" fill="var(--label-black)"/>
    <polygon class="label__red-frame" points="0,0 902,0 902,282 612,282 668,102 0,102" fill="var(--label-red)"/>
    <g role="img" aria-label="Photo of a green tractor working a crop field under a blue sky">
      <polygon points="692,0 902,0 902,130 660,130" fill="url(#tractor-tones)"/>
    </g>
    <g role="img" aria-label="Photo of an orange heavy truck on a highway">
      <polygon points="657,136 902,136 902,274 626,274" fill="url(#truck-tones)"/>
    </g>
    <rect class="label__spec-band" y="350" width="902" height="70" fill="var(--spec-grey)"/>
    <path class="label__brand-panel" d="M540 420 C556 330 604 280 712 274 L902 274 L902 420 Z" fill="var(--label-white)"/>

    <text class="headline headline--slanted" x="308" y="50" font-size="32" fill="var(--label-white)" text-anchor="end" textLength="280" lengthAdjust="spacingAndGlyphs">THE STEADY CHARGE</text>
    <text class="headline headline--slanted" x="308" y="86" font-size="32" fill="var(--label-white)" text-anchor="end" textLength="210" lengthAdjust="spacingAndGlyphs">THAT HOLDS</text>

    <g class="warning-icons">
      <use href="#icon-manual" x="322" y="24" width="44" height="44"/>
      <use href="#icon-goggles" x="382" y="24" width="44" height="44"/>
      <use href="#icon-children" x="440" y="24" width="44" height="44"/>
      <use href="#icon-acid" x="500" y="24" width="44" height="44"/>
      <use href="#icon-explosive" x="558" y="24" width="44" height="44"/>
      <use href="#icon-noflame" x="622" y="24" width="44" height="44"/>
      <path d="M374 20v66M432 20v66M492 20v66M551 20v66M611 20v66" stroke="#ffffff" stroke-opacity="0.5" stroke-width="1"/>
      <g class="icon-caption" font-size="5" text-anchor="middle">
        <text x="344" y="78">READ OPERATING</text><text x="344" y="85">INSTRUCTIONS</text>
        <text x="404" y="78">SHIELD EYES</text><text x="404" y="85">EYE PROTECTION</text>
        <text x="462" y="78">KEEP AWAY</text><text x="462" y="85">FROM CHILDREN</text>
        <text x="522" y="78">NO SMOKING</text><text x="522" y="85">NO SPARKS</text>
        <text x="580" y="78">EXPLOSIVE</text><text x="580" y="85">GASES</text>
        <text x="644" y="78">BATTERY ACID</text><text x="644" y="85">CORROSIVE</text>
      </g>
    </g>

    <text class="headline brand-name" x="30" y="226" font-size="136" fill="var(--label-white)" textLength="610" lengthAdjust="spacingAndGlyphs">VOLTMASTRO</text>
    <rect class="brand-rule" x="28" y="238" width="348" height="10" fill="var(--label-red)"/>
    <text class="headline headline--slanted" x="378" y="272" font-size="44" fill="var(--label-blue)" stroke="#fff" stroke-width="1.5" paint-order="stroke" textLength="284" lengthAdjust="spacingAndGlyphs">BATTERIES</text>
    <text class="headline headline--slanted" x="46" y="336" font-size="54" fill="var(--label-white)" textLength="500" lengthAdjust="spacingAndGlyphs">SUPER HEAVY DUTY</text>

    <g class="maker-name">
      <text class="headline" x="736" y="360" font-size="66" fill="var(--label-blue)" text-anchor="middle" textLength="270" lengthAdjust="spacingAndGlyphs">KORVA</text>
      <text class="headline" x="728" y="396" font-size="24" fill="var(--label-blue)" text-anchor="middle" textLength="290" lengthAdjust="spacingAndGlyphs">POWER SOLUTIONS</text>
    </g>
  </svg>
  <div class="spec">
    <p class="spec__title">Specification:</p>
    <p class="spec__body">Rated 12 V heavy duty starting battery for trucks, tractors and commercial fleets. Check voltage and terminals every service, keep vents clear, charge at the correct rate and store upright in a cool, dry place away from sparks and flame.</p>
  </div>
</section>

<!-- 140 mm label -->
<section class="label label--short">
  <svg viewBox="0 0 902 324" xmlns="http://www.w3.org/2000/svg">
    <rect class="label__base" width="902" height="324" fill="var(--label-black)"/>
    <polygon class="label__red-frame" points="0,0 902,0 902,218 680,218 712,79 0,79" fill="var(--label-red)"/>
    <g role="img" aria-label="Photo of a green tractor working a crop field under a blue sky">
      <polygon points="730,0 902,0 902,104 712,104" fill="url(#tractor-tones)"/>
    </g>
    <g role="img" aria-label="Photo of an orange heavy truck on a highway">
      <polygon points="710,110 902,110 902,214 688,214" fill="url(#truck-tones)"/>
    </g>
    <rect class="label__spec-band" y="272" width="902" height="52" fill="var(--spec-grey)"/>
    <path class="label__brand-panel" d="M594 324 C610 262 650 222 722 216 L902 216 L902 324 Z" fill="var(--label-white)"/>

    <text class="headline headline--slanted" x="28" y="56" font-size="27" fill="var(--label-white)" textLength="364" lengthAdjust="spacingAndGlyphs">THE STEADY CHARGE THAT HOLDS</text>

    <g class="warning-icons">
      <use href="#icon-manual" x="411" y="15" width="38" height="38"/>
      <use href="#icon-goggles" x="457" y="15" width="38" height="38"/>
      <use href="#icon-children" x="503" y="15" width="38" height="38"/>
      <use href="#icon-acid" x="550" y="15" width="38" height="38"/>
      <use href="#icon-explosive" x="597" y="15" width="38" height="38"/>
      <use href="#icon-noflame" x="645" y="15" width="38" height="38"/>
      <path d="M453 12v56M499 12v56M545 12v56M592 12v56M640 12v56" stroke="#ffffff" stroke-opacity="0.5" stroke-width="1"/>
      <g class="icon-caption" font-size="4" text-anchor="middle">
        <text x="430" y="61">READ OPERATING</text><text x="430" y="67">INSTRUCTIONS</text>
        <text x="476" y="61">SHIELD EYES</text><text x="476" y="67">EYE PROTECTION</text>
        <text x="522" y="61">KEEP AWAY</text><text x="522" y="67">FROM CHILDREN</text>
        <text x="569" y="61">NO SMOKING</text><text x="569" y="67">NO SPARKS</text>
        <text x="616" y="61">EXPLOSIVE</text><text x="616" y="67">GASES</text>
        <text x="664" y="61">BATTERY ACID</text><text x="664" y="67">CORROSIVE</text>
      </g>
    </g>

    <text class="headline brand-name" x="46" y="190" font-size="122" fill="var(--label-white)" textLength="560" lengthAdjust="spacingAndGlyphs">VOLTMASTRO</text>
    <rect class="brand-rule" x="46" y="202" width="322" height="9" fill="var(--label-red)"/>
    <text class="headline headline--slanted" x="372" y="234" font-size="40" fill="var(--label-blue)" stroke="#fff" stroke-width="1.5" paint-order="stroke" textLength="272" lengthAdjust="spacingAndGlyphs">BATTERIES</text>
    <text class="headline headline--slanted" x="34" y="264" font-size="40" fill="var(--label-white)" textLength="320" lengthAdjust="spacingAndGlyphs">SUPER HEAVY DUTY</text>

    <g class="maker-name">
      <text class="headline" x="756" y="284" font-size="52" fill="var(--label-blue)" text-anchor="middle" textLength="220" lengthAdjust="spacingAndGlyphs">KORVA</text>
      <text class="headline" x="748" y="312" font-size="20" fill="var(--label-blue)" text-anchor="middle" textLength="228" lengthAdjust="spacingAndGlyphs">POWER SOLUTIONS</text>
    </g>
  </svg>
  <div class="spec">
    <p class="spec__title">Specification:</p>
    <p class="spec__body">Rated 12 V heavy duty starting battery for trucks, tractors and commercial fleets. Check voltage and terminals every service, keep vents clear, charge at the correct rate and store upright in a cool, dry place away from sparks and flame.</p>
  </div>
</section>

</body>
</html>
```